Software company seeks new website design

We are a UK based company called Harbourlight Systems. We build software which helps other businesses to manage their accounts and company finances. All of our clients enjoy full telephone based support as well as access to our software. So, we like to think that we are combining the best accountancy software in the world with a friendly human touch.
We need our homepage completely redesigned. At the moment we have two products which we want to highlight. They are called 'Quick Ledger' (which you can view at www.quickledgr.example) and Tally Beacon.
*VERY IMPORTANT!* We would like the focus of the site to be on our latest new product - Tally Beacon.
We have included a variety of files to help you out, including graphics and some text. Our target audience is medium and large UK based companies who are interested in finding a cost effective and intelligent accountancy solution.
The main call to action on the home page should be EITHER 'learn more', 'find out more' or 'arrange a free demonstration'. If you are unsure about what the text should say then you can use 'Lorem Ipsum'.
Site that we like include:
http://brindlevault.example/
http://www.norvanta.example/
Thank you for viewing. We promise to give constructive feedback to every person who submits a design. Thank you so much. Good luck to you!
IMPORTANT UPDATE: THE PIXEL MARKET WEBSITE KEEPS LOGGING ME OUT WHEN I TRY TO ADD FEEDBACK. I HAVE CONTACTED TECHNICAL SUPPORT AND I'M WAITING FOR A RESOLUTION. I SHALL OFFER FEEDBACK TO EVERY ONE OF YOU AS SOON AS THE PIXEL MARKET WEBSITE IS WORKING PROPERLY
ANOTHER IMPORTANT UPDATE: I SAID ABOVE THAT I'D LIKE THE FOCUS ON THE SITE TO BE ON THE PRODUCT 'TALLY BEACON' - NOT QUICK LEDGER. ONE PERSON HAS ALREADY WASTED TIME BY NOT FOLLOWING THAT INSTRUCTION. SO, ONCE AGAIN - PLEASE MAKE THE FOCUS OF THE SITE ON TALLY BEACON - NOT QUICK LEDGER. THANKS FOLKS. I APPRECIATE YOU BEING HERE.
Reason: Sorry folks, there was a problem with the system which prevented me from leaving any feedback. That problem has now been resolved, however, the guy who is making the final decision is away for a few days. Thank you for everything so far. There's some really great designs so far. Every design will be checked out and given a comment. You have my word.
Reason: Sorry folks, it's been an incredibly busy week and we haven't had time to check the designs out.

```html
<!DOCTYPE html>
<html lang="en">
<head>
<meta charset="utf-8">
<title>Tally Beacon – Home</title>
<link rel="stylesheet" href="https://fonts.googleapis.com/css2?family=PT+Sans:wght@400;700&family=PT+Sans+Narrow&family=Yanone+Kaffeesatz:wght@300&display=swap">
<style>
:root{
  --teal:#0a9fb9;
  --teal-dark:#088aa1;
  --navy:#445675;
  --ink:#333a40;
  --muted:#555;
  --line:#d8d8d8;
  --hero-a:#e6f3f9;
  --hero-b:#cfe6f1;
  --foot-a:#3b4547;
  --foot-b:#1e2426;
  --foot-text:#e6e6e6;
}
*{margin:0;padding:0;box-sizing:border-box}
html,body{width:1120px;height:1200px;overflow:hidden;background:#f4f4f4}
body{position:relative;font-family:"PT Sans",sans-serif;color:var(--ink)}
.page-top-bar{position:absolute;left:160px;top:0;width:800px;height:7px;background:var(--teal)}
.site-header{position:absolute;left:0;top:0;width:1120px;height:104px;background:#fff;border-bottom:1px solid var(--line)}
.brand{position:absolute;left:160px;top:30px;display:flex;align-items:flex-start;gap:12px}
.brand-mark{width:48px;height:48px;background:var(--teal);margin-top:0}
.brand-name{font-family:"PT Sans",sans-serif;font-size:26px;color:var(--navy);line-height:28px}
.brand-tagline{font-size:9.5px;color:var(--navy);margin-top:2px}
.main-nav{position:absolute;left:452px;top:38px;display:flex;font-family:"PT Sans Narrow",sans-serif;font-size:14px;letter-spacing:.3px}
.main-nav a{display:block;height:39px;line-height:40px;color:var(--navy);text-decoration:none;margin-right:24px}
.main-nav a.current{background:var(--navy);color:#fff;padding:0 10px;margin-right:16px}
.hero{position:absolute;left:0;top:104px;width:1120px;height:330px;background:linear-gradient(135deg,var(--hero-a),var(--hero-b));border-bottom:1px solid #c5ccd0}
.hero-art{position:absolute;left:160px;top:0;width:440px;height:330px;background:radial-gradient(ellipse at 60% 60%,#c9dce8,#e2eff6 70%)}
.hero-copy{position:absolute;left:642px;top:48px;width:330px}
.hero-title{font-family:"Yanone Kaffeesatz",sans-serif;font-weight:300;font-size:37px;line-height:40px;color:var(--teal)}
.hero-title span{display:block;color:#2a2f33}
.hero-sub{font-family:"PT Sans",sans-serif;font-size:16px;color:var(--teal);margin-top:10px}
.hero-text{font-family:"PT Sans Narrow",sans-serif;font-size:13px;line-height:18px;color:#444;margin-top:10px}
.btn{display:inline-block;background:var(--teal);color:#fff;font-family:"PT Sans Narrow",sans-serif;font-size:13px;text-decoration:none}
.hero .btn{margin-top:15px;width:78px;height:31px;line-height:31px;text-align:center}
.content-card{position:absolute;left:160px;top:456px;width:800px;height:490px;background:#fff;border-top:6px solid var(--navy);box-shadow:0 1px 3px rgba(0,0,0,.08)}
.intro{position:absolute;left:33px;top:29px;width:735px}
.intro-head{display:flex;align-items:center;gap:8px}
.intro-thumb{width:34px;height:34px;background:linear-gradient(135deg,#d9dcdf,#9aa3aa);border:1px solid #ccc}
.intro-title{font-size:17px;color:#333;letter-spacing:.5px}
.intro p{font-family:"PT Sans Narrow",sans-serif;font-size:11px;line-height:24px;color:#444;margin-top:6px}
.hatch{height:6px;background:repeating-linear-gradient(135deg,#ccc 0 1px,transparent 1px 3px)}
.intro .hatch{margin-top:14px}
.more-link{display:inline-block;margin-top:14px;font-family:"PT Sans Narrow",sans-serif;font-size:11px;color:#222}
.more-link::after{content:"";display:inline-block;margin-left:5px;border-left:4px solid var(--teal);border-top:3px solid transparent;border-bottom:3px solid transparent}
.features{position:absolute;left:15px;top:210px;display:flex;gap:12px}
.feature{width:184px;height:208px;background:#fff;border:1px solid #e2e2e2}
.feature-head{height:98px;text-align:center;padding-top:20px;border-bottom:2px solid #dcdcdc;box-shadow:inset 0 -10px 12px -10px rgba(0,0,0,.08)}
.feature-head svg{display:block;margin:0 auto}
.feature-title{font-size:14.5px;letter-spacing:.8px;margin-top:9px;color:#333}
.feature-body{height:108px;background:#f6f6f6;text-align:center;font-size:11.5px;line-height:21px;color:#555;padding-top:14px;letter-spacing:.2px}
.content-card>.hatch{position:absolute;left:33px;top:454px;width:735px}
.site-footer{position:absolute;left:0;top:978px;width:1120px;height:222px;background:linear-gradient(180deg,var(--foot-a),var(--foot-b));color:var(--foot-text)}
.site-footer::after{content:"";position:absolute;left:0;bottom:0;width:100%;height:7px;background:var(--teal)}
.foot-col{position:absolute;top:36px}
.foot-col h3{font-family:"PT Sans",sans-serif;font-weight:400;font-size:10px;letter-spacing:.6px;color:var(--teal);padding-bottom:4px;border-bottom:1px solid #555e60}
.sitemap{left:186px;width:215px}
.sitemap ul{list-style:none;columns:2;column-gap:0;margin-top:6px}
.sitemap li{font-size:9.5px;line-height:19.2px;padding-left:23px;position:relative}
.sitemap li::before{content:"›";position:absolute;left:7px;color:var(--teal);font-weight:700}
.follow{left:454px;width:214px}
.social{display:grid;grid-template-columns:repeat(3,30px);justify-content:space-between;row-gap:12px;width:166px;margin:14px 0 0 20px}
.social span{width:30px;height:30px;border-radius:50%;background:radial-gradient(circle at 40% 35%,#f4f4f4,#bfc3c4)}
.copyright{font-size:9px;letter-spacing:.5px;margin-top:16px;white-space:nowrap}
.contact{left:728px;width:212px;top:35px}
.contact form{margin-top:4px}
.field{display:flex;margin-bottom:4px}
.field label{width:43px;font-size:9px;padding-top:5px}
.field span{flex:1;height:21px;background:#24292b;border:1px solid #4a5254}
.field.msg span{height:42px}
.contact .btn{margin-left:44px;margin-top:2px;width:48px;height:21px;line-height:21px;text-align:center;font-size:9px;letter-spacing:.5px;border:1px solid #64c3d4}
</style>
</head>
<body>
<div class="site-header">
  <div class="brand">
    <div class="brand-mark"></div>
    <div>
      <div class="brand-name">Tally Beacon</div>
      <div class="brand-tagline">Unlock the potential of your ERP system</div>
    </div>
  </div>
  <nav class="main-nav">
    <a class="current" href="#">HOME</a>
    <a href="#">HOW IT WORKS</a>
    <a href="#">CLIENT TESTIMONIES</a>
    <a href="#">OUR PROMISE</a>
    <a href="#">ABOUT US</a>
    <a href="#">CONTACT US</a>
  </nav>
</div>
<div class="page-top-bar"></div>

<section class="hero">
  <div class="hero-art" role="img" aria-label="Illustration of a cheerful businessman in a suit holding documents, pointing at a rising chart"></div>
  <div class="hero-copy">
    <h1 class="hero-title">A Complete Accounts Dept<span>For An Affordable Price</span></h1>
    <p class="hero-sub">Proin vehicula pulvinar nisi ac semper</p>
    <p class="hero-text">Lorem ipsum dolor sit amet, consectetur adipiscing elit. Praes dolor nunc, rhoncus porttitor bibendum in, placerat sed dui raesent suscipit consequat nunc, et accumsan arcu.</p>
    <a class="btn" href="#">read more</a>
  </div>
</section>

<main class="content-card">
  <article class="intro">
    <div class="intro-head">
      <div class="intro-thumb" role="img" aria-label="Small photo of a hand holding a pen"></div>
      <h2 class="intro-title">Loremed Ipsuine</h2>
    </div>
    <p>Lorem ipsum dolor sit amet, consectetub ono adipisg elit. Praesent dolor nubleno cloom rhobohuson cus porttitorol biben dum in, placerat sed dui raesent.<br>t eros eleifend nisl, id fermentum erat odio quis sapien. Fusce pretium blandit magna vitae rhoncus. Praesent nulla sem, blandit in pellentesque sed, consequat at<br>ligula. Integer et purus erat. Fusce varius, leo non feugiat malesuada, nulla augue hendrerit risus, tempor mattis lacus lacus eu neque. Praesent ultricies lectus a</p>
    <div class="hatch"></div>
    <a class="more-link">read more</a>
  </article>

  <div class="features">
    <div class="feature"><div class="feature-head"><svg width="32" height="32" viewBox="0 0 32 32"><g fill="#0a9fb9"><circle cx="16" cy="16" r="12"/><rect x="13" y="0" width="6" height="32" rx="1"/><rect x="0" y="13" width="32" height="6" rx="1"/><rect x="13" y="0" width="6" height="32" rx="1" transform="rotate(45 16 16)"/><rect x="13" y="0" width="6" height="32" rx="1" transform="rotate(-45 16 16)"/></g><circle cx="16" cy="16" r="6" fill="#fff"/></svg><div class="feature-title">LOREM IPSUM</div></div><div class="feature-body">Donec tempor, risus eu fring<br>la mattis, quam magna ultrices<br>diam, ac scelerisque est ligula<br>in ante ivamus vestibul</div></div>
    <div class="feature"><div class="feature-head"><svg width="32" height="32" viewBox="0 0 32 32"><g fill="#0a9fb9"><circle cx="16" cy="16" r="12"/><rect x="13" y="0" width="6" height="32" rx="1"/><rect x="0" y="13" width="32" height="6" rx="1"/><rect x="13" y="0" width="6" height="32" rx="1" transform="rotate(45 16 16)"/><rect x="13" y="0" width="6" height="32" rx="1" transform="rotate(-45 16 16)"/></g><circle cx="16" cy="16" r="6" fill="#fff"/></svg><div class="feature-title">LOREM IPSUM</div></div><div class="feature-body">Donec tempor, risus eu fring<br>la mattis, quam magna ultrices<br>diam, ac scelerisque est ligula<br>in ante ivamus vestibul</div></div>
    <div class="feature"><div class="feature-head"><svg width="32" height="32" viewBox="0 0 32 32"><g fill="#0a9fb9"><circle cx="16" cy="16" r="12"/><rect x="13" y="0" width="6" height="32" rx="1"/><rect x="0" y="13" width="32" height="6" rx="1"/><rect x="13" y="0" width="6" height="32" rx="1" transform="rotate(45 16 16)"/><rect x="13" y="0" width="6" height="32" rx="1" transform="rotate(-45 16 16)"/></g><circle cx="16" cy="16" r="6" fill="#fff"/></svg><div class="feature-title">LOREM IPSUM</div></div><div class="feature-body">Donec tempor, risus eu fring<br>la mattis, quam magna ultrices<br>diam, ac scelerisque est ligula<br>in ante ivamus vestibul</div></div>
    <div class="feature"><div class="feature-head"><svg width="32" height="32" viewBox="0 0 32 32"><g fill="#0a9fb9"><circle cx="16" cy="16" r="12"/><rect x="13" y="0" width="6" height="32" rx="1"/><rect x="0" y="13" width="32" height="6" rx="1"/><rect x="13" y="0" width="6" height="32" rx="1" transform="rotate(45 16 16)"/><rect x="13" y="0" width="6" height="32" rx="1" transform="rotate(-45 16 16)"/></g><circle cx="16" cy="16" r="6" fill="#fff"/></svg><div class="feature-title">LOREM IPSUM</div></div><div class="feature-body">Donec tempor, risus eu fring<br>la mattis, quam magna ultrices<br>diam, ac scelerisque est ligula<br>in ante ivamus vestibul</div></div>
  </div>
  <div class="hatch"></div>
</main>

<footer class="site-footer">
  <div class="foot-col sitemap">
    <h3>SITEMAP</h3>
    <ul>
      <li>Lorem Ipsum</li><li>Entring</li><li>Solop Ichte</li><li>Opole</li><li>Devrdrics</li><li>Obsoe Palax</li>
      <li>Ferencg Quino</li><li>Susip</li><li>Pnchat Yipol</li><li>Sushiti Oppse</li><li>Fertin Singe</li><li>Poq Weloom</li>
    </ul>
  </div>
  <div class="foot-col follow">
    <h3>FOLLOW US</h3>
    <div class="social" aria-label="Social links">
      <span></span><span></span><span></span><span></span><span></span><span></span>
    </div>
    <p class="copyright">© Copyright 2012 &nbsp;|&nbsp; All rights reserved</p>
  </div>
  <div class="foot-col contact">
    <h3>CONTACT US</h3>
    <form>
      <div class="field"><label>Name</label><span></span></div>
      <div class="field"><label>Email</label><span></span></div>
      <div class="field msg"><label>Message</label><span></span></div>
      <a class="btn">GO</a>
    </form>
  </div>
</footer>
</body>
</html>
```